Create New Bussiness Card For New Shoes Store

Vandrule is a store that sells a variety of skateboard shoes such as Kestro, Mollen etc. we also sell some skateboard and all skateboard accessories.
we like black and white style logo, but also like blue as well.
We are fully assembled with a deck, truck, wheels, and bearings. Add some personality to your board with a fun, graphic skateboard deck. Constructed of thick 7 ply maple,
Target Market(s)
Target audience: 12-40 year old
especially for young man
Industry/Entity Type
Industrial
Contact Information for Business Card
Name: Vandrule
Address1: 2483 Harlow Brisket Rd
City: Xenia
State: Ohio
Zip: 45385
Country: US
Phone: 614830296
email: markolvenby@plimmail.test

```html
<!DOCTYPE html>
<html lang="en">
<head>
<meta charset="utf-8">
<title>Vandrule Business Card</title>
<link rel="stylesheet" href="https://fonts.googleapis.com/css2?family=Source+Sans+3:wght@400;600&display=swap">
<style>
  :root {
    --canvas-bg: #e6e7ea;
    --brand-blue: #1e5fae;
    --brand-black: #161616;
    --panel-light: #f2f3f5;
    --band-white: #ffffff;
    --text-light: #ffffff;
  }
  * { margin: 0; padding: 0; box-sizing: border-box; }
  html, body {
    width: 1200px;
    height: 900px;
    overflow: hidden;
    background: var(--canvas-bg);
    font-family: "Source Sans 3", "Myriad Pro", sans-serif;
  }
  .business-card {
    position: absolute;
    left: 100px;
    top: 140px;
    width: 1000px;
    height: 620px;
    overflow: hidden;
    box-shadow: 0 10px 30px rgba(0,0,0,0.12);
  }
  .card-shapes { position: absolute; inset: 0; }
  .contact-block {
    position: absolute;
    left: 52px;
    top: 172px;
    width: 400px;
    color: var(--text-light);
  }
  .holder-name {
    font-size: 40px;
    font-weight: 400;
    line-height: 1;
  }
  .holder-title {
    font-size: 25px;
    margin-top: 8px;
    line-height: 1;
  }
  .postal-address {
    font-style: normal;
    font-size: 25px;
    line-height: 36px;
    margin-top: 28px;
  }
  .contact-list {
    list-style: none;
    margin-top: 24px;
    font-size: 25px;
    line-height: 36px;
  }
  .contact-list li {
    display: flex;
    align-items: center;
    gap: 14px;
    padding-left: 8px;
    white-space: nowrap;
  }
  .contact-icon { width: 20px; height: 20px; flex: none; }
  .brand-mark {
    position: absolute;
    left: 600px;
    top: 270px;
    width: 360px;
    display: flex;
    align-items: center;
    gap: 14px;
    color: var(--brand-black);
  }
  .brand-dot {
    width: 22px;
    height: 22px;
    border-radius: 50%;
    background: var(--brand-black);
    flex: none;
  }
  .brand-name {
    font-size: 64px;
    font-weight: 400;
    line-height: 1;
  }
</style>
</head>
<body>
  <section class="business-card">
    <svg class="card-shapes" viewBox="0 0 1000 620" width="1000" height="620" aria-hidden="true">
      <rect class="card-base" width="1000" height="620" fill="var(--brand-blue)"/>
      <circle class="accent-band" cx="823" cy="310" r="365" fill="var(--band-white)"/>
      <circle class="accent-line" cx="823" cy="310" r="353" fill="var(--brand-blue)"/>
      <circle class="brand-panel" cx="823" cy="310" r="348" fill="var(--panel-light)"/>
      <rect class="brand-panel-edge" x="823" y="0" width="177" height="620" fill="var(--panel-light)"/>
    </svg>

    <div class="contact-block">
      <h1 class="holder-name">Vandrule</h1>
      <p class="holder-title">Skateboard Shoes &amp; Gear</p>
      <address class="postal-address">
        2483 Harlow Brisket Rd<br>
        Xenia, Ohio 45385, US
      </address>
      <ul class="contact-list">
        <li>
          <svg class="contact-icon" viewBox="0 0 24 24" aria-hidden="true">
            <path fill="#fff" d="M6.6 10.8a15.1 15.1 0 0 0 6.6 6.6l2.2-2.2a1 1 0 0 1 1-.25 11.4 11.4 0 0 0 3.6.57 1 1 0 0 1 1 1V20a1 1 0 0 1-1 1A17 17 0 0 1 3 4a1 1 0 0 1 1-1h3.5a1 1 0 0 1 1 1c0 1.25.2 2.45.57 3.57a1 1 0 0 1-.25 1z"/>
          </svg>
          <span>614830296</span>
        </li>
        <li>
          <svg class="contact-icon" viewBox="0 0 24 24" aria-hidden="true">
            <rect x="2" y="5" width="20" height="14" fill="#fff"/>
            <path d="M2 5l10 8 10-8" fill="none" stroke="var(--brand-blue)" stroke-width="1.8"/>
          </svg>
          <span>markolvenby@plimmail.test</span>
        </li>
        <li>
          <svg class="contact-icon" viewBox="0 0 24 24" aria-hidden="true">
            <g fill="none" stroke="#fff" stroke-width="2.4" stroke-linecap="round">
              <path d="M10 14a4 4 0 0 0 5.7 0l3.6-3.6a4 4 0 0 0-5.7-5.7l-1.2 1.2"/>
              <path d="M14 10a4 4 0 0 0-5.7 0l-3.6 3.6a4 4 0 0 0 5.7 5.7l1.2-1.2"/>
            </g>
          </svg>
          <span>www.vandrule.test</span>
        </li>
      </ul>
    </div>

    <div class="brand-mark">
      <span class="brand-dot"></span>
      <span class="brand-name">Vandrule</span>
    </div>
  </section>
</body>
</html>
```